Business Card/ Email Signature Design Project

I am an Interior Designer. I need a business card that looks sophisticated stylish but simple in design. My work covers space design/ interior architecture/ furniture design/ product development & styling.

I have a very specific brief and know mostly what I want. I'm hoping to work with someone who can translate my ideas.

My branding should have a strong focus on my name, the majority of my work is referral based.
I'm keen to keep a monochromatic colour scheme: dark charcoal/ black/ white/ embossing/ silver. I'm not suggesting we use all that I've listed, they are possible ideas at this stage. I will need to be mindful of printing costs an also how I make the design work across, cards, letter heads, email logo and web design.

Theory behind images sent below;
1-Rug Image_(minus boarder) I was thinking this image could be used on the back of the card with my contact details over. I like that the lines are almost hand drawn and start to look free form. It's a subtle contrast to a more formal front of the card with my name.
2_Owen Ratley_I really like the orientation, the proportion of font on the card, the colour and the font. I like the lower case for my name and the upper case for 'Interior Design'. Not sure if it should be 'Interior Designer or Interior Design' at this stage, was leaning towards 'Interior Design'. Was thinking the 'i' and 'd' in my surname could be the colour eg 'silver'?? We can decide on this once we see it.

Look forward to hearing from you.
Cheers,
Noreen Bastoli

Industry/Entity Type

Printing

Logo Text

Noreen Bastoli Interior Design

```html
<!DOCTYPE html>
<html lang="en">
<head>
<meta charset="utf-8">
<title>Noreen Bastoli Interior Design — Business Card</title>
<link rel="stylesheet" href="https://fonts.googleapis.com/css2?family=Open+Sans:wght@300;600&display=swap">
<style>
  :root {
    --backdrop: #a8a8a8;
    --charcoal: #3a3a3a;
    --paper: #f6f6f6;
    --silver: #c9c9c9;
    --silver-soft: #b4b4b4;
    --ink: #111111;
  }
  * { margin: 0; padding: 0; box-sizing: border-box; }
  html, body {
    width: 1200px;
    height: 900px;
    overflow: hidden;
    background: var(--backdrop);
    font-family: "Open Sans", Arial, sans-serif;
  }
  .layout {
    width: 1200px;
    height: 900px;
    display: flex;
    align-items: center;
    justify-content: center;
    gap: 40px;
  }
  .card {
    position: relative;
    width: 540px;
    height: 310px;
    overflow: hidden;
    box-shadow: 0 6px 18px rgba(0, 0, 0, 0.18);
  }
  .card-line {
    position: absolute;
    inset: 0;
    width: 100%;
    height: 100%;
  }

  /* Front */
  .card-front { background: var(--charcoal); }
  .card-front .line-fill { fill: var(--silver-soft); }
  .front-name {
    position: absolute;
    left: 0;
    right: 0;
    top: 70px;
    text-align: center;
    font-weight: 300;
    color: var(--silver);
  }
  .brand-name {
    display: block;
    font-size: 26px;
    line-height: 1.2;
  }
  .brand-tagline {
    display: block;
    font-size: 13px;
    line-height: 1.4;
    margin-top: 2px;
  }

  /* Back */
  .card-back { background: var(--paper); }
  .back-name {
    position: absolute;
    right: 28px;
    top: 24px;
    text-align: right;
    font-weight: 300;
    color: var(--ink);
  }
  .back-name .brand-name { font-size: 19px; }
  .back-name .brand-tagline { font-size: 11px; margin-top: 0; }
  .contact-list {
    position: absolute;
    left: 34px;
    top: 112px;
    list-style: none;
    font-weight: 600;
    font-size: 15px;
    line-height: 1.3;
    color: var(--ink);
  }
</style>
</head>
<body>
<main class="layout">
  <section class="card card-front" aria-label="Business card front">
    <svg class="card-line" viewBox="0 0 540 310" preserveAspectRatio="none" aria-hidden="true">
      <polygon class="line-fill" points="0,232 540,150 540,162 0,244"/>
    </svg>
    <div class="front-name">
      <span class="brand-name">Noreen Bastoli</span>
      <span class="brand-tagline">Interior Design</span>
    </div>
  </section>

  <section class="card card-back" aria-label="Business card back">
    <div class="back-name">
      <span class="brand-name">Noreen Bastoli</span>
      <span class="brand-tagline">Interior Design</span>
    </div>
    <ul class="contact-list">
      <li>Address: PO Box 472 Brunswick VIC. 3056</li>
      <li>Email: interiors@noreenbastoli.com</li>
      <li>Web: www.noreenbastoli.com</li>
      <li>Mobile: 0400 555 019</li>
    </ul>
  </section>
</main>
</body>
</html>
```